Stationary for 2-office law firm with global theme

I need stationary with contact info for two offices. I'd like the same letterhead design to work for printing on stationary and also for digital use in Word. The colors and feel should match the new logo, which is a stylized globe with and "F" in it. I'd also like envelopes with an eye-catching design.

Target Market(s)

U.S. citizens seeking dual citizenship with Italy or Ireland

Industry/Entity Type

Law

Font styles to use
Serif
Sans Serif
Other font styles liked:
• To match the logo?

Colors
0054AA
0677BA
7BADD7
CADEEF
E8F1F8

Requirements
Must have
• Clean, modern design incorporating new logo

```html
<!DOCTYPE html>
<html lang="en">
<head>
<meta charset="utf-8">
<title>Marveni Law – Letterhead</title>
<link rel="stylesheet" href="https://fonts.googleapis.com/css2?family=Open+Sans:wght@400&family=Roboto:wght@400;700&display=swap">
<style>
  :root {
    --backdrop: #dddddd;
    --paper: #f8f8f8;
    --navy: #123d6b;
    --sky: #29a8df;
    --body-text: #555555;
    --contact-text: #5a5a5a;
    --white: #ffffff;
    --signature-tone: #e6e6e6;
  }
  * { box-sizing: border-box; margin: 0; padding: 0; }
  html, body {
    width: 1153px;
    height: 1200px;
    overflow: hidden;
    background: var(--backdrop);
  }
  .letterhead {
    position: absolute;
    left: 147px;
    top: 0;
    width: 859px;
    height: 1200px;
    background: var(--paper);
    font-family: "Open Sans", Arial, sans-serif;
  }
  .brand {
    position: absolute;
    left: 68px;
    top: 63px;
    display: flex;
    align-items: center;
    gap: 18px;
  }
  .brand-dot {
    width: 86px;
    height: 86px;
    border-radius: 50%;
    background: var(--sky);
  }
  .brand-name {
    font-family: "Roboto", Arial, sans-serif;
    font-weight: 700;
    font-size: 40px;
    line-height: 1;
    color: var(--navy);
    letter-spacing: -0.5px;
  }
  .contact {
    position: absolute;
    left: 580px;
    top: 58px;
    font-family: "Roboto", Arial, sans-serif;
    font-size: 18px;
    line-height: 22px;
    color: var(--contact-text);
  }
  .contact-address { margin-bottom: 6px; }
  .contact-line {
    display: flex;
    align-items: center;
    gap: 7px;
  }
  .contact-icon { width: 16px; height: 14px; flex: none; }
  .letter-body {
    position: absolute;
    left: 77px;
    top: 254px;
    width: 704px;
    font-size: 16px;
    line-height: 23px;
    color: var(--body-text);
    text-align: justify;
  }
  .letter-body p { margin-bottom: 23px; }
  .letter-body .salutation, .letter-body .closing { text-align: left; }
  .signature {
    position: absolute;
    left: 77px;
    top: 885px;
    width: 102px;
    height: 96px;
    background: var(--signature-tone);
  }
  .footer-band {
    position: absolute;
    left: 0;
    bottom: 0;
    width: 859px;
    height: 26px;
    font-family: "Roboto", Arial, sans-serif;
    font-size: 17px;
    color: var(--white);
  }
  .footer-shapes { position: absolute; inset: 0; }
  .footer-office {
    position: absolute;
    left: 77px;
    top: 2px;
    line-height: 22px;
  }
  .footer-web {
    position: absolute;
    left: 648px;
    top: 2px;
    line-height: 22px;
  }
</style>
</head>
<body>
  <main class="letterhead">
    <header>
      <div class="brand">
        <span class="brand-dot"></span>
        <span class="brand-name">MARVENI LAW</span>
      </div>
      <address class="contact" style="font-style:normal">
        <div class="contact-address">48 Harbor Lane, Suite 5<br>Milford, MA 01757</div>
        <div class="contact-line">
          <svg class="contact-icon" viewBox="0 0 16 14" aria-hidden="true">
            <path d="M1 5 Q8 -1 15 5 L13 7 L11 5 L5 5 L3 7 Z" fill="var(--sky)"/>
            <rect x="3" y="7" width="10" height="6" rx="1" fill="var(--sky)"/>
          </svg>
          <span>+15550142208</span>
        </div>
        <div class="contact-line">
          <svg class="contact-icon" viewBox="0 0 16 14" aria-hidden="true">
            <path d="M1 5 L8 1 L15 5 L15 13 L1 13 Z" fill="var(--sky)"/>
            <path d="M1 5 L8 10 L15 5" fill="none" stroke="var(--white)" stroke-width="1.4"/>
          </svg>
          <span>info@marvenilaw.com</span>
        </div>
      </address>
    </header>

    <section class="letter-body">
      <p class="salutation">Dear customer,</p>
      <p>Lorem ipsum dolor sit amet, consectetur adipisicing elit, sed do eiusmod tempor incididunt ut labore et dolore magna aliqua. Ut enim ad minim veniam, quis nostrud exercitation ullamco laboris nisi ut aliquip ex ea commodo consequat. Duis aute irure dolor in reprehenderit in voluptate velit esse cillum dolore eu fugiat nulla pariatur. Excepteur sint occaecat cupidatat non proident, sunt in culpa qui officia deserunt mollit anim id est laborum.</p>
      <p>Lorem ipsum dolor sit amet, consectetur adipisicing elit, sed do eiusmod tempor incididunt ut labore et dolore magna aliqua. Ut enim ad minim veniam, quis nostrud exercitation ullamco laboris nisi ut aliquip ex ea commodo consequat. Duis aute irure dolor in reprehenderit in voluptate velit esse cillum dolore eu fugiat nulla pariatur. Excepteur sint occaecat cupidatat non proident, sunt in culpa qui officia deserunt mollit anim id est laborum.</p>
      <p>Lorem ipsum dolor sit amet, consectetur adipisicing elit, sed do eiusmod tempor incididunt ut labore et dolore magna aliqua. Ut enim ad minim veniam, quis nostrud exercitation ullamco laboris nisi ut aliquip ex ea commodo consequat. Duis aute irure dolor in reprehenderit in voluptate velit esse cillum dolore eu fugiat nulla pariatur. Excepteur sint occaecat cupidatat non proident, sunt in culpa qui officia deserunt mollit anim id est laborum.</p>
      <p>Lorem ipsum dolor sit amet, consectetur adipisicing elit, sed do eiusmod tempor incididunt ut labore et dolore magna aliqua. Ut enim ad minim veniam, quis nostrud exercitation ullamco laboris nisi ut aliquip ex ea commodo consequat. Duis aute irure dolor in reprehenderit.</p>
      <p class="closing">Yours Sincerely,</p>
    </section>

    <div class="signature" role="img" aria-label="Handwritten signature of the sender"></div>

    <footer class="footer-band">
      <svg class="footer-shapes" viewBox="0 0 859 26" preserveAspectRatio="none" aria-hidden="true">
        <polygon points="0,0 632,0 607,26 0,26" fill="var(--sky)"/>
        <polygon points="638,0 859,0 859,26 613,26" fill="var(--navy)"/>
      </svg>
      <span class="footer-office">New York Office : 48 Harbor Lane, Suite 5 Milford, MA 01757</span>
      <span class="footer-web">www.marvenilaw.com</span>
    </footer>
  </main>
</body>
</html>
```